New Business card design to reflect rebrand

I would like a business card design with a good base colour for our new logo and also a placeholder for a profile pic of the card holder. the design needs to be editable to the point that we can easily change the picture of the person and use that design for printlarkly etc. we are looking at a metalic finish business card so will need a good base colour to bring out the finish.

Target Market(s)

prospective customers

Industry/Entity Type

Business

Contact Information for Business Card

I would like one editable design that we can change the name of the card holder and profile picture. The design need to be in a format that be send to printlarkly etc.

Our address is Fenwick Lodge, Mill Lane, Ashworth Green, KT14 3WB Tel no. 01632 960418

Requirements
Must have
• place holder for a profile pic for the card holder. in AI or preferably PSD format

```html
<!DOCTYPE html>
<html lang="en">
<head>
<meta charset="utf-8">
<title>Brightel Workplace Services – Business Card</title>
<link rel="stylesheet" href="https://fonts.googleapis.com/css2?family=Montserrat:wght@500;600;700&family=Open+Sans:wght@400;600&display=swap">
<style>
  :root {
    --slate: #435a78;
    --white: #ffffff;
    --ink: #2b2b2b;
    --stage: #e9e7e3;
    --photo-top: #c9ccd2;
    --photo-bottom: #3c4656;
  }
  * { box-sizing: border-box; margin: 0; padding: 0; }
  html, body { width: 1200px; height: 900px; overflow: hidden; }
  body {
    background: var(--stage);
    display: flex;
    flex-direction: column;
    align-items: center;
    justify-content: center;
    gap: 36px;
    font-family: "Open Sans", sans-serif;
  }
  .card {
    position: relative;
    width: 700px;
    height: 400px;
    overflow: hidden;
    box-shadow: 0 6px 18px rgba(0,0,0,0.18);
  }

  /* Back face */
  .card--back {
    background: var(--slate);
    display: flex;
    align-items: center;
    justify-content: center;
  }
  .brand-back {
    text-align: center;
    color: var(--white);
    font-family: "Montserrat", sans-serif;
    font-weight: 600;
  }
  .brand-back__name { font-size: 52px; letter-spacing: 3px; line-height: 1; }
  .brand-back__sub { font-size: 20px; letter-spacing: 6px; margin-top: 6px; }

  /* Front face */
  .card--front { background: var(--white); }
  .front-band { position: absolute; inset: 0; }
  .profile-photo {
    position: absolute;
    left: 60px;
    top: 28px;
    width: 330px;
    height: 284px;
    background: linear-gradient(180deg, var(--photo-top) 0%, var(--photo-bottom) 100%);
  }
  .brand-front {
    position: absolute;
    left: 424px;
    top: 50px;
    display: flex;
    align-items: center;
    gap: 10px;
    color: var(--slate);
    font-family: "Montserrat", sans-serif;
    font-weight: 700;
  }
  .brand-front__mark { width: 18px; height: 18px; background: var(--slate); flex: none; }
  .brand-front__text { line-height: 1.05; }
  .brand-front__name { font-size: 34px; letter-spacing: 1px; }
  .brand-front__sub { font-size: 12.5px; letter-spacing: 3.2px; }
  .contact {
    position: absolute;
    left: 420px;
    top: 168px;
    list-style: none;
    font-size: 15px;
    color: var(--ink);
  }
  .contact li { display: flex; align-items: center; gap: 8px; margin-bottom: 4px; }
  .contact svg { width: 13px; height: 13px; fill: var(--slate); }
  .address {
    position: absolute;
    left: 430px;
    top: 248px;
    color: var(--white);
    font-size: 15px;
    line-height: 1.45;
  }
  .holder-name {
    position: absolute;
    left: 60px;
    bottom: 30px;
    color: var(--white);
    font-family: "Montserrat", sans-serif;
    font-weight: 700;
    font-size: 32px;
    letter-spacing: 1px;
  }
</style>
</head>
<body>

  <section class="card card--back" aria-label="Card back">
    <div class="brand-back">
      <div class="brand-back__name">BRIGHTEL</div>
      <div class="brand-back__sub">WORKPLACE SERVICES</div>
    </div>
  </section>

  <section class="card card--front" aria-label="Card front">
    <svg class="front-band" viewBox="0 0 700 400" preserveAspectRatio="none" aria-hidden="true">
      <polygon points="0,312 390,312 410,232 700,232 700,400 0,400" fill="var(--slate)"/>
    </svg>

    <div class="profile-photo" role="img" aria-label="Profile photo of the card holder"></div>

    <div class="brand-front">
      <span class="brand-front__mark"></span>
      <div class="brand-front__text">
        <div class="brand-front__name">BRIGHTEL</div>
        <div class="brand-front__sub">WORKPLACE SERVICES</div>
      </div>
    </div>

    <ul class="contact">
      <li>
        <svg viewBox="0 0 24 24"><path d="M6.6 10.8a15.1 15.1 0 0 0 6.6 6.6l2.2-2.2a1 1 0 0 1 1-.25 11.4 11.4 0 0 0 3.6.57 1 1 0 0 1 1 1V20a1 1 0 0 1-1 1A17 17 0 0 1 3 4a1 1 0 0 1 1-1h3.5a1 1 0 0 1 1 1c0 1.25.2 2.45.57 3.6a1 1 0 0 1-.25 1z"/></svg>
        01632 960418
      </li>
      <li>
        <svg viewBox="0 0 24 24"><path d="M2 5h20v14H2z M2 5l10 8 10-8" fill="var(--slate)" stroke="var(--white)" stroke-width="1.5"/></svg>
        info@brightel-ws.com
      </li>
    </ul>

    <p class="address">Fenwick Lodge, Mill Lane,<br>Ashworth Green, KT14 3WB</p>

    <h1 class="holder-name">DANIEL HART</h1>
  </section>

</body>
</html>
```